Stationary & Business Cards
TRB Weddings & Events by Greta
You need to extend the project before designers can submit more proposals, right now it is locked. Thank you! :)
And we need business cards, stationary & envelopes.
They like a zen feel...cherry blossoms...birds...
Thank you for all of your submissions. The owners do not like the purple logo anymore and have completly changed it. We have uploaded a eps file for it. This project is guaranteed and we will be picking a winner. If you have time please submit new designs. Thank you.
Your eps file is an image please upload orignal Ai file.
-Thanks
Please upload ai or eps of your logo.

```html
<!DOCTYPE html>
<html lang="en">
<head>
<meta charset="utf-8">
<title>TRB Weddings &amp; Events by Greta — Stationery</title>
<link href="https://fonts.googleapis.com/css2?family=Questrial&display=swap" rel="stylesheet">
<style>
  :root {
    --leaf: #a3cc45;
    --leaf-soft: #c9e39a;
    --leaf-pale: #e6f2cf;
    --ink: #4a4a4a;
    --paper: #ffffff;
    --edge: #bdbdbd;
  }
  * { box-sizing: border-box; margin: 0; padding: 0; }
  html, body { width: 1200px; height: 1101px; overflow: hidden; background: var(--paper); }
  body { position: relative; font-family: "Questrial", "Helvetica Neue", Arial, sans-serif; color: var(--ink); }

  .sheet { position: absolute; background: var(--paper); border: 1px solid var(--edge); overflow: hidden; }

  .brand { position: absolute; display: flex; flex-direction: column; align-items: flex-start; }
  .brand-mark { background: var(--leaf); border-radius: 8px; }
  .brand-name { color: var(--ink); white-space: nowrap; margin-top: 6px; }

  .vine { position: absolute; background: radial-gradient(ellipse at top right, var(--leaf) 0%, var(--leaf-soft) 45%, rgba(255,255,255,0) 75%); }

  .band { position: absolute; left: 0; right: 0; bottom: 0; background: var(--leaf); color: var(--paper); text-align: center; }

  /* Letterhead */
  .letterhead { left: 24px; top: 30px; width: 750px; height: 1041px; }
  .letterhead .brand { left: 84px; top: 30px; }
  .letterhead .brand-mark { width: 66px; height: 66px; }
  .letterhead .brand-name { font-size: 15px; }
  .letterhead .vine { right: 0; top: 0; width: 250px; height: 200px; }
  .letterhead .band { height: 78px; padding-top: 16px; font-size: 12px; line-height: 20px; }

  /* Business card front */
  .card-front { left: 876px; top: 36px; width: 294px; height: 174px; }
  .card-front .brand { left: 18px; top: 16px; }
  .card-front .brand-mark { width: 40px; height: 40px; border-radius: 5px; }
  .card-front .brand-name { font-size: 8px; margin-top: 3px; }
  .card-front .person { position: absolute; left: 150px; top: 22px; font-size: 10px; line-height: 14px; color: var(--leaf); }
  .card-front .person .role { color: var(--ink); font-size: 8px; }
  .card-front .band { height: 66px; padding-top: 12px; font-size: 8px; line-height: 13px; }

  /* Business card back */
  .card-back { left: 876px; top: 228px; width: 294px; height: 177px; background: linear-gradient(135deg, var(--leaf-soft), var(--leaf)); border-color: var(--leaf); }
  .card-back .vine-field { position: absolute; inset: 0; background: radial-gradient(ellipse at 20% 30%, rgba(255,255,255,0.35), rgba(255,255,255,0) 60%), radial-gradient(ellipse at 85% 80%, rgba(255,255,255,0.3), rgba(255,255,255,0) 55%); }
  .card-back .ghost-name { position: absolute; left: 0; right: 0; top: 70px; text-align: center; font-size: 28px; color: rgba(255,255,255,0.55); letter-spacing: 2px; }

  /* Envelope */
  .envelope { left: 480px; top: 570px; width: 690px; height: 405px; }
  .envelope .flap { position: absolute; left: 0; top: 0; }
  .envelope .flap-name { position: absolute; left: 0; right: 0; top: 40px; text-align: center; font-size: 20px; color: rgba(255,255,255,0.7); letter-spacing: 2px; }
  .envelope .brand { left: 45px; top: 165px; }
  .envelope .brand-mark { width: 66px; height: 66px; }
  .envelope .brand-name { font-size: 15px; }
  .envelope .vine { right: 0; top: 110px; width: 260px; height: 200px; background: radial-gradient(ellipse at 70% 40%, var(--leaf) 0%, var(--leaf-soft) 40%, rgba(255,255,255,0) 72%); }
  .envelope .band { height: 45px; padding-top: 14px; font-size: 12px; }
</style>
</head>
<body>

<section class="sheet letterhead">
  <div class="brand">
    <div class="brand-mark"></div>
    <div class="brand-name">TRB Weddings &amp; Events by Greta</div>
  </div>
  <div class="vine" role="img" aria-label="Green leafy vine ornament trailing from the top right corner"></div>
  <footer class="band">
    Harbor Point, CA P: 555-204-3188<br>
    greta@trbeventsstudio.com www.trbeventsstudio.com
  </footer>
</section>

<section class="sheet card-front">
  <div class="brand">
    <div class="brand-mark"></div>
    <div class="brand-name">TRB Weddings &amp; Events by Greta</div>
  </div>
  <div class="person">Greta Halvorsen<div class="role">Event Consultant</div></div>
  <footer class="band">
    Harbor Point, CA P: 555-204-3188<br>
    greta@trbeventsstudio.com<br>
    www.trbeventsstudio.com
  </footer>
</section>

<section class="sheet card-back">
  <div class="vine-field" role="img" aria-label="Pale green leaf and vine pattern across the card back"></div>
  <div class="ghost-name">TRB</div>
</section>

<section class="sheet envelope">
  <svg class="flap" width="690" height="150" viewBox="0 0 690 150" aria-hidden="true">
    <path d="M0 0 H690 V40 C560 60 430 140 345 140 C260 140 130 60 0 40 Z" fill="var(--leaf)"/>
  </svg>
  <div class="flap-name">TRB</div>
  <div class="brand">
    <div class="brand-mark"></div>
    <div class="brand-name">TRB Weddings &amp; Events by Greta</div>
  </div>
  <div class="vine" role="img" aria-label="Green leafy vine ornament on the right side of the envelope"></div>
  <footer class="band">Harbor Point, CA</footer>
</section>

</body>
</html>
```